Tasman Curdworks Guild needs new business cards

We need new business cards designed and produced. We are likely to need other design work done for ads, flyers etc in future.

We would like to start with an initial business card.

The Tasman Curdworks Guild (TCG) is a membership-based not-for-profit organisation that looks after the interests of Australia's small to medium artisan cheesemakers, many of whom are also small-scale farmers. The design should be simple, using our logo, but also communicate our artisan cheese and small dairy farm focus.

The first card to be designed and produced is for me, Miriam Tolhurst. My details are:

Miriam Tolhurst
Secretary
Tasman Curdworks Guild (TCG)
http://www.curdworksguild.example
T +61452837190
E miriam.miriamtolhurst@mailbox.example

I have attached the TCG logo in jpg form. I have a higher resolution version available if needed.

Thank you!

Miriam

Miriam Tolhurst
Tasman Curdworks Guild
miriam.miriamtolhurst@mailbox.example
+61452837190

Sans Serif

• Logo (see attached file)

```html
<!DOCTYPE html>
<html lang="en">
<head>
<meta charset="utf-8">
<title>Tasman Curdworks Guild – Business Card</title>
<link rel="stylesheet" href="https://fonts.googleapis.com/css2?family=Marcellus&family=Tinos&display=swap">
<style>
  :root {
    --backdrop: #e8e5e0;
    --card: #ffffff;
    --brown: #5b3518;
    --cheese: #f9c96b;
    --cheese-soft: #fde9c0;
  }
  * { margin: 0; padding: 0; box-sizing: border-box; }
  html, body {
    width: 1200px;
    height: 892px;
    overflow: hidden;
    background: var(--backdrop);
  }
  .business-card {
    position: absolute;
    left: 100px;
    top: 160px;
    width: 1000px;
    height: 572px;
    background: var(--card);
    box-shadow: 0 10px 30px rgba(0, 0, 0, 0.12);
  }
  .brand {
    position: absolute;
    left: 64px;
    top: 52px;
    display: flex;
    align-items: flex-start;
    gap: 28px;
  }
  .brand-dot {
    width: 112px;
    height: 112px;
    border-radius: 50%;
    background: var(--cheese);
    flex: none;
  }
  .brand-name {
    font-family: "Marcellus", serif;
    font-size: 40px;
    line-height: 44px;
    letter-spacing: 2px;
    color: var(--brown);
  }
  .holder {
    position: absolute;
    left: 200px;
    top: 250px;
  }
  .holder-name {
    font-family: "Tinos", serif;
    font-size: 66px;
    line-height: 70px;
    color: var(--brown);
  }
  .holder-role {
    font-family: "Tinos", serif;
    font-size: 30px;
    letter-spacing: 2px;
    color: var(--cheese);
    margin-top: 2px;
  }
  .contact {
    position: absolute;
    left: 200px;
    top: 380px;
    list-style: none;
    font-family: "Tinos", serif;
    font-size: 27px;
    line-height: 40px;
    color: var(--brown);
  }
  .spot-accent {
    position: absolute;
    right: 60px;
    bottom: 50px;
    width: 170px;
    height: 190px;
    border-radius: 12px;
    background: radial-gradient(circle at 50% 50%, var(--cheese-soft), var(--card) 75%);
  }
</style>
</head>
<body>
  <main class="business-card">
    <header class="brand">
      <span class="brand-dot" aria-hidden="true"></span>
      <p class="brand-name">Tasman<br>Curdworks<br>Guild</p>
    </header>
    <section class="holder">
      <h1 class="holder-name">Miriam Tolhurst</h1>
      <p class="holder-role">Secretary</p>
    </section>
    <ul class="contact">
      <li>+61452837190</li>
      <li>miriam.miriamtolhurst@mailbox.example</li>
      <li>www.curdworksguild.example</li>
    </ul>
    <div class="spot-accent" role="img" aria-label="Scattered brown and cheese-yellow dots decoration"></div>
  </main>
</body>
</html>
```